Business card design for modern law firm

We need new business cards. Information about our law firm can be found at www.qrtl-recht.de. The business cards should include the information that we have offices in Berlin and Stuttgart. They should be customizable for all attorneys who are partially located in Berlin and partially in Stuttgart. Example of the information:
Jonas Ackermann
lawyer
Specialist lawyer for copyright and media law
Lindenweg 17, 70374 Stuttgart
ackermann@qrtl-recht.de
+49 711 483 15 260
www.qrtl-recht.de
It is important for us that we can edit the cards independently, i.e. exchange names and contact details.
In addition, a QR code for a VCard should be placed on the card.
The design of the old maps is attached; the new design should clearly distinguish itself from them. They should be more modern. The design is ideally based on the design of the website www.qrtl-recht.de.
Industry/Entity Type
Rechtsanwalt
Contact Information for Business Card
Siehe projektbeschreibung

```html
<!DOCTYPE html>
<html lang="de">
<head>
<meta charset="utf-8">
<title>QRTL Rechtsanwälte – Visitenkarte</title>
<link rel="stylesheet" href="https://fonts.googleapis.com/css2?family=Manrope:wght@400;500;700;800&display=swap">
<style>
  :root {
    --brand-green: #a6ce39;
    --text-grey: #6b6b6b;
    --card-white: #ffffff;
    --backdrop: #e4e4e4;
    --placeholder: #e9efd9;
  }
  * { box-sizing: border-box; margin: 0; padding: 0; }
  html, body {
    width: 1200px;
    height: 1200px;
    overflow: hidden;
    background: var(--backdrop);
    font-family: "Manrope", Arial, sans-serif;
  }
  .canvas { position: relative; width: 1200px; height: 1200px; }

  .card {
    position: absolute;
    left: 175px;
    width: 848px;
    height: 519px;
    background: var(--card-white);
    overflow: hidden;
  }
  .card--front { top: 57px; }
  .card--back  { top: 616px; }

  .accent-bar { position: absolute; background: var(--brand-green); }
  .accent-bar--top    { left: 0;     top: 71px;  width: 462px; height: 33px; }
  .accent-bar--bottom { left: 546px; top: 451px; width: 302px; height: 32px; }

  .firm-name {
    position: absolute;
    color: var(--brand-green);
    font-weight: 500;
    letter-spacing: 0.04em;
    line-height: 1;
  }
  .firm-name--front { left: 546px; top: 78px; font-size: 74px; }

  .person-name {
    position: absolute;
    left: 79px; top: 208px;
    font-size: 38px;
    font-weight: 800;
    color: var(--brand-green);
    letter-spacing: -0.005em;
  }
  .person-role {
    position: absolute;
    left: 79px; top: 256px;
    font-size: 21px;
    color: var(--text-grey);
  }
  .person-specialty {
    position: absolute;
    left: 79px; top: 285px;
    font-size: 16px;
    color: var(--text-grey);
  }

  .contact-list, .address {
    position: absolute;
    list-style: none;
    font-size: 22px;
    font-style: normal;
    color: var(--text-grey);
    line-height: 33px;
  }
  .contact-list { left: 79px; top: 337px; }
  .contact-list li { display: flex; align-items: center; }
  .contact-icon { width: 15px; height: 15px; margin-right: 21px; flex: none; }

  .address { left: 546px; display: flex; }
  .address--berlin    { top: 240px; }
  .address--stuttgart { top: 337px; }
  .address .contact-icon { margin-top: 12px; margin-right: 14px; }

  .back-lockup {
    position: absolute;
    left: 0; right: 0; top: 212px;
    text-align: center;
    line-height: 1;
  }
  .back-lockup__name {
    display: block;
    font-size: 40px;
    font-weight: 700;
    letter-spacing: 0.12em;
    color: var(--brand-green);
  }
  .back-lockup__tagline {
    display: block;
    margin-top: 14px;
    font-size: 22px;
    font-weight: 700;
    letter-spacing: 0.1em;
    color: var(--text-grey);
  }
  .vcard-code {
    position: absolute;
    right: 48px; bottom: 44px;
    width: 104px; height: 104px;
    background: var(--placeholder);
    border: 2px solid var(--brand-green);
  }
</style>
</head>
<body>
<main class="canvas">

  <section class="card card--front" aria-label="Vorderseite">
    <div class="accent-bar accent-bar--top"></div>
    <div class="firm-name firm-name--front">QRTL</div>

    <h1 class="person-name">Jonas Ackermann</h1>
    <p class="person-role">lawyer</p>
    <p class="person-specialty">Specialist lawyer for copyright and media law</p>

    <ul class="contact-list">
      <li>
        <svg class="contact-icon" viewBox="0 0 16 16" aria-hidden="true">
          <rect x="1" y="3" width="14" height="10" rx="1.5" fill="var(--brand-green)"/>
          <path d="M2 4.5 L8 9 L14 4.5" fill="none" stroke="#fff" stroke-width="1.3"/>
        </svg>
        ackermann@qrtl-recht.de
      </li>
      <li>
        <svg class="contact-icon" viewBox="0 0 16 16" aria-hidden="true">
          <path d="M3.5 1.5 L6 1.5 L7 5 L5.3 6.3 C6.2 8.3 7.7 9.8 9.7 10.7 L11 9 L14.5 10 L14.5 12.5 C14.5 13.6 13.6 14.5 12.5 14.5 C6.9 14.5 1.5 9.1 1.5 3.5 C1.5 2.4 2.4 1.5 3.5 1.5 Z" fill="var(--brand-green)"/>
        </svg>
        +49 711 483 15 260
      </li>
      <li>
        <svg class="contact-icon" viewBox="0 0 16 16" aria-hidden="true">
          <circle cx="8" cy="8" r="6.5" fill="none" stroke="var(--brand-green)" stroke-width="1.8"/>
          <path d="M1.5 8 H14.5 M8 1.5 C5 5 5 11 8 14.5 M8 1.5 C11 5 11 11 8 14.5" fill="none" stroke="var(--brand-green)" stroke-width="1.3"/>
        </svg>
        www.qrtl-recht.de
      </li>
    </ul>

    <address class="address address--berlin">
      <svg class="contact-icon" viewBox="0 0 16 16" aria-hidden="true">
        <path d="M8 0.5 C4.7 0.5 2.5 2.9 2.5 5.8 C2.5 9.6 8 15.5 8 15.5 C8 15.5 13.5 9.6 13.5 5.8 C13.5 2.9 11.3 0.5 8 0.5 Z" fill="var(--brand-green)"/>
        <circle cx="8" cy="5.8" r="2" fill="#fff"/>
      </svg>
      <span>Kastanienallee 8,<br>10435 Berlin</span>
    </address>

    <address class="address address--stuttgart">
      <svg class="contact-icon" viewBox="0 0 16 16" aria-hidden="true">
        <path d="M8 0.5 C4.7 0.5 2.5 2.9 2.5 5.8 C2.5 9.6 8 15.5 8 15.5 C8 15.5 13.5 9.6 13.5 5.8 C13.5 2.9 11.3 0.5 8 0.5 Z" fill="var(--brand-green)"/>
        <circle cx="8" cy="5.8" r="2" fill="#fff"/>
      </svg>
      <span>Lindenweg 17,<br>70374 Stuttgart</span>
    </address>

    <div class="accent-bar accent-bar--bottom"></div>
  </section>

  <section class="card card--back" aria-label="Rückseite">
    <div class="back-lockup">
      <span class="back-lockup__name">QRTL RECHTSANWÄLTE</span>
      <span class="back-lockup__tagline">LEGAL SERVICES PartmbB</span>
    </div>
    <div class="vcard-code" role="img" aria-label="vCard QR code area"></div>
  </section>

</main>
</body>
</html>
```